Creative label for amber glass candle jar.

We are a candle company. Our products are handmade by us and natural. We are looking for something minimalistic and unique. We need a label for our candle jars (amber glass with black lid). Our current label doesn't match these requirements. We would like our products to be stocked in London shop, therefore design has to be up to a high standard. Jar specification Diameter (mm) 65 Height without cap (mm) 80. We want the new design to be different from the current one. It's just a guide for wording.
We should be able adjust the label, to change scent name.
Our scents are
*Coconut & Vanilla
*Lavender
*Bergamot
*Italian Garden
*Hygge
*Eucalyptus & Peppermint
*Coffee
*Cedarwood & Juniperberry
To know more about us, visit our website www.wrenfieldcandles.com or instagram.com/wrenfieldcandles
Good luck!
Industry/Entity Type
It Company
Colors
Designer to choose colors to be used in the design.
Requirements
Must have
- * I have attached two of our logos, label design must include one of them.
- *has to mention that it's made in London
- *has to say that candle is natural/made with essential oils
- *has to have scent name and No. on it..
- Label can be vertical or horizontal, but has to be square/rectangular,.
Should not have
- Label should not be round

```html
<!DOCTYPE html>
<html lang="en">
<head>
<meta charset="utf-8">
<title>Wrenfield — Lavender No. 2 Candle Label</title>
<link rel="stylesheet" href="https://fonts.googleapis.com/css2?family=Cutive&display=swap">
<style>
  :root {
    --label-sage: #c8cdc5;
    --ink: #141414;
    --rule-width: 4px;
  }
  html, body {
    margin: 0;
    padding: 0;
    overflow: hidden;
    background: var(--label-sage);
  }
  .label {
    position: relative;
    width: 900px;
    height: 1200px;
    background: var(--label-sage);
    color: var(--ink);
    font-family: "Cutive", "Courier New", serif;
    overflow: hidden;
  }
  .label__frame {
    position: absolute;
    left: 112px;
    top: 130px;
    width: 672px;
    height: 946px;
    box-sizing: border-box;
    border: var(--rule-width) solid var(--ink);
  }
  .label__divider {
    position: absolute;
    left: 0;
    right: 0;
    top: 698px;
    border-top: var(--rule-width) solid var(--ink);
  }
  .brand-name {
    position: absolute;
    left: 0;
    right: 0;
    top: 140px;
    margin: 0;
    text-align: center;
    font-size: 104px;
    font-weight: 400;
    line-height: 1;
    letter-spacing: 2px;
  }
  .scent-name {
    position: absolute;
    left: 0;
    right: 0;
    top: 424px;
    margin: 0;
    text-align: center;
    font-size: 90px;
    font-weight: 400;
    line-height: 1;
  }
  .scent-number {
    position: absolute;
    left: 428px;
    top: 580px;
    margin: 0;
    font-size: 56px;
    line-height: 1;
  }
  .claim {
    position: absolute;
    left: 0;
    right: 0;
    margin: 0;
    text-align: center;
    line-height: 1;
  }
  .claim--natural {
    top: 752px;
    font-size: 48px;
  }
  .claim--oils {
    top: 834px;
    font-size: 42px;
  }
  .origin {
    position: absolute;
    left: 0;
    right: 0;
    top: 1118px;
    margin: 0;
    text-align: center;
    font-size: 38px;
    font-variant: small-caps;
    line-height: 1;
  }
</style>
</head>
<body>
  <main class="label">
    <div class="label__frame">
      <h1 class="brand-name">wrenfield</h1>
      <h2 class="scent-name">Lavender</h2>
      <p class="scent-number">No. 2</p>
      <div class="label__divider"></div>
      <p class="claim claim--natural">100% NATURAL</p>
      <p class="claim claim--oils">Made with essential oils</p>
    </div>
    <p class="origin">Made In London</p>
  </main>
</body>
</html>
```